Einfache Webside für kleine Promotion- und Personalagentur
Zielgruppe
Lumo Staffing ist eine international tätige Promotion- und Personalagentur. Wir bieten auch im Bereich Sport der jew. Sportart affine Hostessen und Hosts f an.
Aufgabenstellung
Wir hatten bis dato eine sehr gute Auftragslage und leider keine Zeit für eine Homepage. Wir suchen jemaden der uns das Design für die Seite übernimmt und Online stellt. Wir sind auch offen wenn dies über z.B. Q+Z erfolgt. Auf den jeweiligen Seiten wollen wir den Text dann immer selbst eintragen. Seiten: Startseite mit Buttons zu folgenden Feldern: Promotion (Text mit Erklärung was wir machen und Bildern), Personal (Text mit Erklärung was wir machen und Bilder - die Bilder sollten austauschbar sein), Team, Referenzen, Kontaktseite, Gästebuch, Impressum. Die Seite sollte Modern aussehen und nicht zu überladen sein.

```html
<!DOCTYPE html>
<html lang="de">
<head>
<meta charset="utf-8">
<title>Lumo Staffing – Promotion</title>
<link rel="stylesheet" href="https://fonts.googleapis.com/css2?family=Source+Sans+3:wght@400;600;700&display=swap">
<style>
  :root {
    --teal: #7ecbd6;
    --slate: #8b959d;
    --slate-dark: #7d878f;
    --mist: #ebedef;
    --text: #8a9299;
    --white: #ffffff;
  }
  * { box-sizing: border-box; margin: 0; padding: 0; }
  html, body { width: 1200px; height: 1167px; overflow: hidden; background: var(--white); }
  body { font-family: "Source Sans 3", "Source Sans Pro", sans-serif; color: var(--text); }

  .site-header { height: 143px; display: flex; align-items: center; justify-content: center; gap: 14px; }
  .brand-mark { width: 88px; height: 88px; border-radius: 50%; background: var(--slate); }
  .brand-name { font-size: 44px; font-weight: 600; color: var(--teal); letter-spacing: -0.5px; }

  .main-nav { height: 75px; background: var(--slate); }
  .main-nav ul { list-style: none; display: flex; margin-left: 176px; height: 100%; }
  .main-nav li { width: 121px; display: flex; align-items: center; justify-content: center;
    border-right: 1px solid var(--slate-dark); color: var(--white); font-weight: 700; font-size: 13.5px; letter-spacing: 0.3px; }
  .main-nav li.active { background: var(--teal); }
  .accent-band { height: 13px; background: var(--teal); }

  .breadcrumb { height: 41px; background: var(--mist); display: flex; align-items: center; justify-content: center;
    gap: 14px; font-size: 13px; color: var(--text); }
  .breadcrumb .current { color: var(--teal); }

  .content { padding: 20px 0 0 173px; width: 1060px; height: 450px; }
  .page-title { font-size: 37px; font-weight: 400; color: var(--teal); line-height: 1.2; letter-spacing: 0.3px; }
  .page-lead { font-size: 19.5px; font-weight: 400; line-height: 1.38; margin-top: 2px; }
  .content p { font-size: 12.4px; line-height: 16px; margin-top: 16px; }
  .content p.first { margin-top: 33px; }
  .section-title { font-size: 19.5px; font-weight: 400; color: var(--teal); margin-top: 38px; }
  .section-title + p { margin-top: 16px; }

  .gallery { height: 238px; background: var(--mist); display: flex; align-items: center; justify-content: center; gap: 26px; }
  .gallery-arrow { width: 30px; height: 34px; }
  .gallery-arrow.prev { margin-right: 4px; }
  .gallery-arrow.next { margin-left: 4px; }
  .gallery-photo { width: 235px; height: 158px; }
  .photo-street { background: linear-gradient(160deg, #9a5a44, #8a8f92 70%); }
  .photo-stand { background: linear-gradient(160deg, #b04a3e, #d8b04c 60%, #9a6a3c); }
  .photo-store { background: linear-gradient(160deg, #d9d6c6, #5a5450 55%, #c04a3a); }

  .footer-band { height: 10px; background: var(--teal); }
  .site-footer { height: 171px; background: var(--slate); color: var(--white); display: flex; padding: 26px 0 0 176px; font-size: 13px; line-height: 20.3px; }
  .footer-address { width: 301px; }
  .footer-links { width: 295px; list-style: none; font-weight: 700; }
  .strong { font-weight: 700; }
  .follow-title { font-size: 20px; font-weight: 400; line-height: 1; margin-top: -1px; }
  .social-list { display: flex; gap: 7px; margin-top: 12px; }
  .social-list span { width: 45px; height: 45px; border-radius: 50%; background: var(--white); }
</style>
</head>
<body>
  <header class="site-header">
    <span class="brand-mark"></span>
    <span class="brand-name">Lumo Staffing</span>
  </header>

  <nav class="main-nav">
    <ul>
      <li class="active">PROMOTION</li>
      <li>PERSONAL</li>
      <li>TEAM</li>
      <li>REFERENZEN</li>
      <li>GÄSTEBUCH</li>
      <li>KONTAKT</li>
      <li>IMPRESSUM</li>
    </ul>
  </nav>
  <div class="accent-band"></div>

  <div class="breadcrumb"><span>Home</span><span>&gt;</span><span class="current">Promotion</span></div>

  <main class="content">
    <h1 class="page-title">PROMOTION - LOREM IPSUM</h1>
    <h2 class="page-lead">LOREM IPSUM DOLOR SIT AMET, CONSETETUR SADIPSCING,<br>ELITR SED DIAM NONUMY EIRMOD TEMPOR ET DOLORE.</h2>
    <p class="first">Lorem ipsum dolor sit amet, consetetur sadipscing elitr, sed diam nonumy eirmod tempor invidunt ut labore et dolore magna aliquyam erat, sed diam voluptua. At vero eos et accusam et justo duo dolores et ea rebum. Stet clita kasd gubergren, no sea takimata sanctus est Lorem ipsum dolor sit amet dolor sit amet. Lorem ipsum dolor sit amet, consetetur sadipscing elitr, sed diam nonumy eirmod tempor invidunt ut labore et dolore magna aliquyam erat, sed diam voluptua. At vero eos et accusam et justo duo dolores et ea rebum.</p>
    <p>Lorem ipsum dolor sit amet, consetetur sadipscing elitr, sed diam nonumy eirmod tempor invidunt ut labore et dolore magna aliquyam erat, sed diam voluptua. At vero eos et accusam et justo duo dolores et ea rebum. Stet clita kasd gubergren, no sea takimata sanctus est Lorem ipsum dolor sit amet dolor sit amet. Lorem ipsum dolor sit amet, consetetur sadipscing elitr, sedt, consetetur sadipscing elitr diam nonumy eirmod tempor invidunt ut labore et dolore magna aliquyam erat, sed diam voluptua. At vero eos et accusam et justo duo dolores et ea rebum.</p>
    <h3 class="section-title">EIRMOD TEMPOR ET DOLORE.</h3>
    <p>At vero eos et accusam et justo duo dolores et ea rebum. Stet clita kasd gubergren, no sea takimata sanctus est Lorem ipsum dolor sit amet dolor sit amet. Lorem ipsum dolor sit amet, consetetur sadipscing elitr, sedt, consetetur sadipscing elitr diam nonumy eirmod tempor invidunt ut labore et dolore magna aliquyam erat, sed diam voluptua. At vero eos et accusam et justo duo dolores et ea rebum.</p>
  </main>

  <section class="gallery">
    <svg class="gallery-arrow prev" viewBox="0 0 30 34" aria-label="Zurück"><path d="M18 0 L26 0 L12 17 L26 34 L18 34 L4 17 Z" fill="var(--teal)"/></svg>
    <div class="gallery-photo photo-street" role="img" aria-label="Promoter in roter Schürze spricht vor einer Bäckerei mit einem Passanten"></div>
    <div class="gallery-photo photo-stand" role="img" aria-label="Zwei Promoterinnen an einem Aktionsstand mit Luftballons in einer Bäckerei"></div>
    <div class="gallery-photo photo-store" role="img" aria-label="Zwei Promoterinnen in roten Schürzen in einem Verkaufsraum"></div>
    <svg class="gallery-arrow next" viewBox="0 0 30 34" aria-label="Weiter"><path d="M12 0 L4 0 L18 17 L4 34 L12 34 L26 17 Z" fill="var(--teal)"/></svg>
  </section>

  <div class="footer-band"></div>
  <footer class="site-footer">
    <address class="footer-address" style="font-style:normal">
      <div class="strong">LUMO STAFFING GMBH</div>
      <div>Musterstraße 21</div>
      <div>56786 Musterhausen</div>
      <div>&nbsp;</div>
      <div>info@lumostaffing.de</div>
      <div>www.lumo-staffing.de</div>
    </address>
    <ul class="footer-links">
      <li>PROMOTION</li><li>PERSONAL</li><li>TEAM</li><li>REFERENZEN</li><li>GÄSTEBUCH</li><li>KONTAKT</li><li>IMPRESSUM</li>
    </ul>
    <div class="footer-social">
      <div class="follow-title">FOLGE UNS</div>
      <div class="social-list"><span></span><span></span><span></span></div>
    </div>
  </footer>
</body>
</html>
```